Home Based Business Website Design

Need 1 template web design. Require clean friendly website design that helps promote a Homeward business opportunity based around personal development. The site should lean towards appealing to the female market (see target market) and be straight forward, fresh colours and good use of white space. The site should have a family focus using imagery of happy families and reinforcing the quality of life and freedom available. The site should be in a two or three column format, navigation can be top or left, there will be 6 menu items in total (E.g. home, about, testimonials, contact, faq, why me?). There should be space for a video, text, images and a clear "call to action" (contact us). The site should come across as professiona, positive, friendly and trustworthy. Scope for many more sites of this nature in the future.

Target Market(s)

People that are ready for change. People wanting to make money from a business at home. 25+ years old, mum's , professional. People that are tired of the commute and want a better quality of life. While the site should lean towards focusing on stay at home mums or working mums looking for a better life it should also be able to appeal to a wider audience (male and female) so should not be too "girly"!

Industry/Entity Type

Business

Requirements
Must have
• Fairly open to interpretation, site must have at least two columns, clear call to action, space for a video, text and images, navigation (single level 6 items).
Nice to have
• Possibly animated banner of images?
Should not have
• Try to use less obvious imagery no stressed out executives or people jumping for joy. no dark designs no purple or flouro colours. Site should be modern in design.

```html
<!DOCTYPE html>
<html lang="en">
<head>
<meta charset="utf-8">
<title>Homeward – Home Based Business</title>
<link rel="stylesheet" href="https://fonts.googleapis.com/css2?family=PT+Sans:ital,wght@0,400;0,700;1,400;1,700&display=swap">
<style>
:root{
  --page-bg-top:#d9d8e6;
  --page-bg-bottom:#f1f1f6;
  --frame:#a9a6d8;
  --white:#ffffff;
  --navy:#35335f;
  --nav-dark:#3b3968;
  --nav-light:#7d7bc4;
  --lilac:#8f8ce8;
  --lilac-soft:#9a99f5;
  --lilac-pale:#d6d5fa;
  --video-border:#8c89d4;
  --body-text:#1c2a5c;
  --coral:#d97c7c;
  --copyright:#a7a4ea;
}
*{box-sizing:border-box;margin:0;padding:0}
html,body{width:1200px;height:1121px;overflow:hidden}
body{
  background:linear-gradient(180deg,var(--page-bg-top),var(--page-bg-bottom));
  font-family:"PT Sans",Tahoma,sans-serif;
}
.stage{
  position:absolute;left:0;top:0;width:1100px;height:1028px;
  transform:scale(1.090909);transform-origin:0 0;
}
.site{
  position:absolute;left:101px;top:12px;width:898px;height:1000px;
  background:var(--white);border:2px solid var(--frame);
}
.abs{position:absolute}

/* header */
.logo{
  left:30px;top:40px;font-size:70px;font-weight:700;color:var(--navy);
  letter-spacing:-1px;line-height:1;
}
.hero-photo{
  left:413px;top:0;width:468px;height:176px;
  background:linear-gradient(90deg,#eceff1 0%,#dfe3e4 45%,#c7cccc 100%);
}

/* navigation */
.main-nav{
  left:1px;top:176px;width:892px;height:37px;border-radius:3px;
  background:linear-gradient(180deg,var(--nav-dark),var(--nav-light));
  display:flex;align-items:center;padding-left:4px;
}
.main-nav a{
  color:var(--white);font-weight:700;font-size:18px;text-decoration:none;
  padding:0 16px;line-height:29px;border-left:1px solid rgba(255,255,255,.25);
}
.main-nav a:first-child{border-left:none}

/* text */
.section-title{font-size:16px;font-weight:700;color:var(--lilac)}
.copy{font-size:13px;line-height:21px;color:var(--body-text)}
.copy p+p{margin-top:21px}

/* left column */
.intro-title{left:33px;top:234px}
.intro-copy{left:33px;top:270px;width:392px}
.call-box{
  left:29px;top:549px;width:379px;height:76px;background:var(--lilac-soft);
  color:var(--white);padding:6px 0 0 21px;
}
.call-box .label{font-size:16px;font-weight:700}
.call-box .number{font-size:32px;font-weight:700;line-height:34px}
.call-box .sub{font-size:18px;line-height:18px}
.reason-photo{
  left:32px;top:646px;width:378px;height:288px;
  background:linear-gradient(160deg,#f4f4f4 0%,#d9d6d3 50%,#b9b1a8 100%);
}
.reason-link{
  left:170px;top:648px;width:222px;text-align:right;
  font-size:18px;font-weight:700;line-height:22px;color:var(--lilac);
}
.reason-link u{color:#8380d0}

/* right column */
.register-box{
  left:484px;top:230px;width:377px;height:76px;background:var(--coral);
  color:var(--white);font-size:25px;line-height:31px;padding:6px 0 0 11px;
}
.register-box u{font-weight:700}
.video-box{
  left:485px;top:323px;width:374px;height:230px;
  background:var(--lilac-pale);border:3px solid var(--video-border);
}
.video-box .caption{position:absolute;left:6px;top:4px;font-size:18px;color:#111}
.video-thumb{
  position:absolute;left:63px;top:30px;width:254px;height:173px;
  background:linear-gradient(135deg,#3f6b2a,#7fa34b 55%,#c97d4a);
}
.video-thumb svg{position:absolute;left:95px;top:50px}
.more-title{left:481px;top:575px}
.more-copy{left:481px;top:611px;width:392px}
.quote-box{
  left:480px;top:769px;width:170px;height:105px;text-align:center;
  background:linear-gradient(180deg,var(--white),#c4c3f2);padding-top:8px;
}
.quote-box .quote{font-size:17px;font-style:italic;color:var(--lilac);line-height:21px}
.quote-box .more{font-size:15px;font-weight:700;color:#9896e6;line-height:17px;margin-top:4px}
.family-photo{
  left:646px;top:781px;width:232px;height:153px;
  background:linear-gradient(180deg,#ffffff 0%,#efe6df 60%,#e0d2c6 100%);
}

/* footer */
.site-footer{
  left:1px;top:934px;width:892px;height:37px;border-radius:3px;
  background:linear-gradient(180deg,var(--nav-dark),#5c5a99);
  display:flex;justify-content:center;align-items:center;gap:16px;
}
.site-footer a{color:var(--white);font-size:13px;text-decoration:none}
.copyright{right:18px;top:979px;font-size:12px;color:var(--copyright)}
</style>
</head>
<body>
<div class="stage">
  <div class="site">
    <header>
      <div class="abs logo">Homeward</div>
      <div class="abs hero-photo" role="img" aria-label="Smiling woman lying on a white sofa working on a laptop"></div>
      <nav class="abs main-nav">
        <a href="#">Home</a><a href="#">About us</a><a href="#">Testimonials</a><a href="#">Contact</a><a href="#">Faq</a><a href="#">Why me?</a>
      </nav>
    </header>

    <main>
      <h2 class="abs section-title intro-title">Lorem ipsum dolor sit amet</h2>
      <div class="abs copy intro-copy">
        <p>Consectetur adipiscing elit. Nullam fringilla lobortis velit at porttitor. Duis iaculis felis et nisi facilisis at ultricies diam pellentesque. Nunc id nibh metus. Quisque at est vestibulum ante pulvinar hendrerit eget in sapien. Nunc vel lobortis erat. Nunc non sem mi. Sed auctor dolor sit amet quam porta ut congue elit imperdiet.</p>
        <p>Duis varius interdum nulla eget facilisis. Integer sollicitudin metus in eros malesuada nec dapibus nunc tincidunt. Phasellus in mauris sed turpis ultricies accumsan. Duis ac risus risus, vel interdum leo. Suspendisse ultricies convallis ante a hendrerit. Sed libero turpis, volutpat quis condimentum eu, bibendum ac quam. Nulla nec nibh et erat commodo elementum quis a nisi. Sed consectetur arcu</p>
      </div>

      <div class="abs call-box">
        <span class="label">Call us on:</span> <span class="number">0800 246 1357</span>
        <div class="sub">To find out how you can earn more now!</div>
      </div>

      <div class="abs reason-photo" role="img" aria-label="Smiling young man on a sofa using a laptop"></div>
      <div class="abs reason-link"><u>Click here</u> to find out why you should try this</div>

      <div class="abs register-box"><u>Register here</u> to help us help you start your new, easier life!</div>

      <div class="abs video-box">
        <div class="caption">Watch our 60 second clip:</div>
        <div class="video-thumb" role="img" aria-label="Happy family lying on grass with heads together">
          <svg width="72" height="72" viewBox="0 0 72 72" aria-hidden="true">
            <circle cx="36" cy="36" r="36" fill="#ffffff" fill-opacity=".8"/>
            <path d="M27 18 L54 36 L27 54 Z" fill="#4a4a4a"/>
          </svg>
        </div>
      </div>

      <h2 class="abs section-title more-title">Sed suscipit purus nulla, eget dictum libero.</h2>
      <div class="abs copy more-copy">
        <p>Proin quis nisl libero. Vivamus egestas tempus elit, at placerat urna convallis nec. Sed malesuada, leo vitae tristique aliquam, mauris massa vehicula tortor, in ullamcorper purus mi vitae magna. Nullam sit amet luctusneque. Vestibulum vel elit nec justo hendrerit imperdiet. Suspendisse eget lorem eget leo iaculis feugiat. Ut non est est. Mauris vitae mi ut diam tempor aliquet.</p>
      </div>

      <div class="abs quote-box">
        <div class="quote">"I wish I had<br>started sooner!"</div>
        <div class="more">Read our members'<br>testimonials...</div>
      </div>
      <div class="abs family-photo" role="img" aria-label="Smiling mother and young daughter"></div>
    </main>

    <footer class="abs site-footer">
      <a href="#">Sitemap</a><a href="#">Privacy policy</a><a href="#">Terms &amp; Conditions</a><a href="#">Contact us</a>
    </footer>
    <div class="abs copyright">Copyright 2009</div>
  </div>
</div>
</body>
</html>
```